I need a Professional Eye-Catching Paperback and e-Book Cover Design done with different mockups

I need a Professional Eye-Catching e-Book Cover Design done with different mockups

I need 2-3 designs to choose from per designer.

Book title - Harbor Ledger:

Subtitle - Growing riches that stay behind you

Author name - K. Dapo Renke

I have attached some sample designs but i need you to be creative.

```html
<!DOCTYPE html>
<html lang="en">
<head>
<meta charset="utf-8">
<title>Harbor Ledger — Book Cover</title>
<link rel="stylesheet" href="https://fonts.googleapis.com/css2?family=Oswald:wght@300;400;500;600&display=swap">
<style>
  :root {
    --stage: #333333;
    --navy: #253e7e;
    --navy-deep: #23418f;
    --royal: #2c52c4;
    --cyan: #00b6de;
    --cyan-light: #a7e6f4;
    --white: #ffffff;
  }
  html, body {
    margin: 0;
    padding: 0;
    width: 1200px;
    height: 1001px;
    overflow: hidden;
    background: var(--stage);
  }
  .book-cover {
    position: absolute;
    left: 297px;
    top: 72px;
    width: 606px;
    height: 857px;
    display: block;
  }
  .title-accent { font-family: "Oswald", sans-serif; font-weight: 300; fill: var(--cyan); }
  .title-main { font-family: "Oswald", sans-serif; font-weight: 400; fill: var(--white); }
  .subtitle { font-family: "Oswald", sans-serif; font-weight: 500; fill: var(--cyan); }
  .author { font-family: "Oswald", sans-serif; font-weight: 500; fill: var(--white); letter-spacing: 5px; }
</style>
</head>
<body>
<svg class="book-cover" viewBox="0 0 757 1070" xmlns="http://www.w3.org/2000/svg">
  <defs>
    <linearGradient id="photoTone" x1="0" y1="0" x2="1" y2="1">
      <stop offset="0" stop-color="#22408c"/>
      <stop offset="0.6" stop-color="#2a4db3"/>
      <stop offset="1" stop-color="#2f57cc"/>
    </linearGradient>
    <linearGradient id="photoFade" x1="0" y1="0" x2="0" y2="1">
      <stop offset="0" stop-color="white" stop-opacity="0"/>
      <stop offset="0.3" stop-color="white" stop-opacity="1"/>
    </linearGradient>
    <mask id="photoMask">
      <rect x="0" y="540" width="757" height="530" fill="url(#photoFade)"/>
    </mask>
    <linearGradient id="ringTone" x1="0.9" y1="0.05" x2="0.15" y2="0.95">
      <stop offset="0" stop-color="var(--cyan-light)"/>
      <stop offset="1" stop-color="var(--cyan)"/>
    </linearGradient>
    <linearGradient id="bandTone" x1="0" y1="0" x2="1" y2="0">
      <stop offset="0" stop-color="var(--cyan)"/>
      <stop offset="1" stop-color="var(--cyan-light)"/>
    </linearGradient>
    <clipPath id="coverClip">
      <rect x="0" y="0" width="757" height="1070"/>
    </clipPath>
  </defs>

  <g clip-path="url(#coverClip)">
    <rect class="cover-ground" x="0" y="0" width="757" height="1070" fill="var(--navy)"/>

    <rect class="cityscape-photo" role="img" aria-label="Photo of glass office towers seen from below, tinted blue"
          x="0" y="540" width="757" height="530" fill="url(#photoTone)" mask="url(#photoMask)"/>

    <path class="lower-band" fill="url(#bandTone)" fill-rule="evenodd"
          d="M387 -280 a680 680 0 1 0 0.01 0 Z M387 -215 a615 615 0 1 1 -0.01 0 Z"/>

    <circle class="main-ring" cx="387" cy="375" r="348" fill="none" stroke="url(#ringTone)" stroke-width="44"/>
    <rect class="ring-tab" x="0" y="375" width="40" height="160" fill="var(--cyan)" opacity="0.85"/>

    <text class="title-accent" x="283" y="266" font-size="145" textLength="302" lengthAdjust="spacingAndGlyphs">HARBOR</text>
    <text class="title-main" x="142" y="506" font-size="285" textLength="490" lengthAdjust="spacingAndGlyphs">Ledger</text>
    <text class="subtitle" x="146" y="590" font-size="28" textLength="390" lengthAdjust="spacingAndGlyphs">GROWING RICHES THAT STAY BEHIND YOU</text>
    <text class="author" x="378" y="662" font-size="32" text-anchor="middle">K. DAPO RENKE</text>
  </g>
</svg>
</body>
</html>
```